Southland Rig Academy needs a modern website that oozes professionalism

Our current website is boring and looks like everyone elses. We need a modern website that says we are the best at plant operator training. We use Ironvale and Darvento equipment for our training. We train all over Australia in Civil Construction, Mining and Quarrying. We want to be the "Go to" website for all plant operator training in Australia.

Industry/Entity Type

Heavy Machinery Training

Colors
0054AA
0677BA
7BADD7
CADEEF
E8F1F8
FFF300
FFF600
FEFA6F
FFFEC7
FFFEE8

```html
<!DOCTYPE html>
<html lang="en">
<head>
<meta charset="utf-8">
<title>Southland Rig Academy</title>
<link href="https://fonts.googleapis.com/css2?family=Libre+Baskerville:wght@400;700&family=Fira+Sans:wght@500;600;700&family=Open+Sans:wght@400;600;700&display=swap" rel="stylesheet">
<style>
:root{
  --navy:#173f7a;
  --navy-deep:#143768;
  --blue:#0054aa;
  --field:#5b7fb4;
  --yellow:#f8c400;
  --ink:#3a3f4a;
  --muted:#6d717a;
  --pale:#f4f5f7;
  --line:#e4e6ea;
  --white:#fff;
}
*{box-sizing:border-box;margin:0;padding:0}
html,body{width:1200px;height:4841px;overflow:hidden}
body{position:relative;background:var(--white);font-family:"Open Sans",sans-serif;color:var(--ink)}
.abs{position:absolute}
.serif{font-family:"Libre Baskerville",serif;font-weight:700;color:var(--navy)}
.sans-h{font-family:"Fira Sans",sans-serif;font-weight:600;color:var(--navy)}
.photo{position:absolute;overflow:hidden}
.label{position:absolute;font-size:11px;font-weight:600;letter-spacing:.5px;color:var(--yellow);text-transform:uppercase;display:flex;align-items:center;gap:12px}
.label .bar{display:inline-block;width:48px;height:2px;background:var(--yellow)}
.btn{position:absolute;background:var(--yellow);color:var(--white);font-size:12px;font-weight:700;display:flex;align-items:center;justify-content:center;border-radius:3px}
p.body{font-size:12.5px;line-height:24px;color:var(--ink)}

/* header */
.topbar{left:0;top:0;width:1200px;height:34px;background:#f1f2f4}
.topbar .welcome{position:absolute;left:392px;top:10px;font-size:13px;color:#333}
.topbar .divider{position:absolute;left:592px;top:6px;width:1px;height:22px;background:#c9ccd2}
.topbar .mail{position:absolute;left:626px;top:4px;display:flex;align-items:center;gap:8px;font-size:13px;color:#333}
.ico-circle{width:26px;height:26px;border-radius:50%;border:2px solid var(--navy);display:flex;align-items:center;justify-content:center}
.nav{left:0;top:34px;width:1200px;height:52px;background:var(--white)}
.nav a{position:absolute;top:20px;font-size:13px;color:#333;text-decoration:none}
.nav a.active{color:var(--yellow);font-weight:600}
.logo-oval{left:148px;top:0;width:160px;height:98px;border-radius:50%;background:var(--white);box-shadow:0 4px 12px rgba(0,0,0,.15);display:flex;align-items:center;justify-content:center;gap:8px}
.brand-dot{width:22px;height:22px;border-radius:50%;background:var(--navy);flex:none}
.brand-name{font-family:"Open Sans",sans-serif;font-weight:700;color:var(--navy);font-size:11px;line-height:13px;letter-spacing:.3px}
.callbox{left:864px;top:0;width:193px;height:86px;background:var(--navy);color:var(--white);padding:20px 0 0 52px}
.callbox .ico{position:absolute;left:14px;top:26px;width:34px;height:34px;border-radius:50%;border:2px solid var(--white);display:flex;align-items:center;justify-content:center}
.callbox small{display:block;font-size:14px}
.callbox strong{display:block;font-size:19px;font-weight:600;margin-top:3px}

/* hero */
.hero-photo{left:0;top:86px;width:1200px;height:780px;background:linear-gradient(160deg,#5a5856 0%,#7d7976 40%,#9a948d 60%,#6f6a64 100%)}
.hero-card{left:77px;top:272px;width:541px;height:359px;background:var(--white);padding:52px 0 0 45px}
.hero-card .accent{position:absolute;left:0;top:56px;width:6px;height:104px;background:var(--yellow)}
.hero-card h1{font-size:55px;line-height:66px}
.hero-card p{font-size:11.5px;line-height:22px;color:#555;margin-top:14px;width:410px}

/* about */
.about-text{left:623px;top:990px;width:450px}
.about-text h2{font-size:38px;line-height:60px;margin-top:30px}
.about-text p{margin-top:20px}

/* features */
.features{left:92px;top:1536px;width:1010px;height:210px;background:var(--white);border-radius:0 0 70px 70px;box-shadow:0 10px 30px rgba(0,0,0,.08)}
.feature{position:absolute;top:36px;width:290px}
.feature .fi{position:absolute;left:0;top:0;width:62px;height:62px;border-radius:50%;border:2.5px solid var(--navy);display:flex;align-items:center;justify-content:center}
.feature h3{position:absolute;left:80px;top:8px;font-size:21px}
.feature .sub{position:absolute;left:82px;top:40px;font-size:15px;color:var(--navy)}
.feature p{position:absolute;left:80px;top:74px;font-size:12.5px;line-height:24px;width:200px}

/* services */
.slider-btn{position:absolute;width:46px;height:62px;background:var(--white);box-shadow:0 3px 10px rgba(0,0,0,.12);display:flex;align-items:center;justify-content:center}
.svc-card{position:absolute;top:2150px;width:278px;height:198px;background:var(--white);box-shadow:0 6px 20px rgba(0,0,0,.08);padding:26px 0 0 37px}
.svc-card.dark{background:var(--navy)}
.svc-card h3{font-size:19px}
.svc-card p{font-size:12px;line-height:24px;color:#666;margin-top:14px;width:220px}
.svc-card .more{display:block;margin-top:12px;font-size:14px;font-weight:700;color:var(--yellow)}
.svc-card.dark h3,.svc-card.dark p,.svc-card.dark .more{color:var(--white)}
.outline-btn{left:500px;top:2391px;width:191px;height:45px;border:2px solid var(--yellow);border-radius:23px;color:var(--yellow);font-size:13px;font-weight:600;display:flex;align-items:center;justify-content:center}

/* projects */
.projects{left:0;top:2507px;width:1200px;height:654px;background:var(--pale)}
.proj-bar{left:248px;top:3007px;width:599px;height:75px;background:var(--white);display:flex;align-items:center;padding-left:40px;font-family:"Fira Sans",sans-serif;font-weight:600;font-size:23px;color:var(--blue)}
.proj-arrow{left:847px;top:3007px;width:79px;height:75px;background:var(--yellow);display:flex;align-items:center;justify-content:center}
.side-btn{position:absolute;top:2881px;width:66px;height:90px;background:var(--white);display:flex;align-items:center;justify-content:center}

/* testimonials */
.t-card{position:absolute;top:3390px;width:321px;height:263px;background:var(--white);box-shadow:0 4px 18px rgba(0,0,0,.07);text-align:center;padding-top:72px}
.t-card .stars{color:#f0a21a;font-size:20px;letter-spacing:8px}
.t-card p{font-size:12.5px;line-height:24px;color:#777;margin:18px auto 0;width:240px}
.avatar{position:absolute;width:68px;height:68px;border-radius:50%;top:3358px;border:3px solid var(--white);box-shadow:0 2px 6px rgba(0,0,0,.15)}
.quote{position:absolute;top:3620px;width:66px;height:46px;border-radius:33px 33px 0 0;background:var(--yellow);display:flex;align-items:flex-start;justify-content:center;padding-top:8px;color:var(--white);font-family:"Libre Baskerville",serif;font-size:30px;line-height:30px;font-weight:700}
.t-name{position:absolute;top:3690px;width:321px;text-align:center;font-size:17px;font-weight:600;color:#3a3a3a}
.t-place{position:absolute;top:3720px;width:321px;text-align:center;font-size:13px;color:#888}

/* contact */
.contact-card{left:650px;top:3981px;width:462px;height:470px;background:var(--navy);border:6px solid var(--white);border-radius:10px;box-shadow:0 6px 20px rgba(0,0,0,.15);text-align:center;padding-top:40px;color:var(--white)}
.contact-card h2{font-family:"Fira Sans",sans-serif;font-size:28px;font-weight:600}
.contact-card p{font-size:10.5px;line-height:17px;width:370px;margin:8px auto 0}
.field{position:absolute;left:28px;width:394px;height:43px;background:var(--field);border-radius:3px;font-size:10px;color:var(--white);text-align:left;padding:15px 0 0 27px;letter-spacing:.3px}
.submit{position:absolute;left:28px;top:381px;width:394px;height:44px;background:var(--white);border-radius:3px;color:var(--navy);font-weight:700;font-size:14px;display:flex;align-items:center;justify-content:center}

/* footer */
.fcol{position:absolute;top:4555px}
.fcol h4{font-size:14px;font-weight:400;color:var(--yellow)}
.fcol .rule{width:118px;height:1px;background:var(--line);margin:14px 0 18px}
.fcol ul{list-style:none;font-size:14px;line-height:32px;color:#444}
.fcol .row{display:flex;align-items:center;gap:16px;font-size:14px;color:#444;line-height:22px;margin-bottom:14px}
.social{display:flex;align-items:center;gap:10px;font-size:14px;color:#333}
.social span.c{width:24px;height:24px;border-radius:50%;background:#e9eaec}
</style>
</head>
<body>

<!-- header -->
<div class="abs topbar">
  <span class="welcome">WELCOME</span>
  <span class="divider"></span>
  <span class="mail"><span class="ico-circle"><svg width="13" height="10" viewBox="0 0 13 10"><rect x="0.75" y="0.75" width="11.5" height="8.5" fill="none" stroke="#173f7a" stroke-width="1.5"/><path d="M1 1l5.5 4.5L12 1" fill="none" stroke="#173f7a" stroke-width="1.5"/></svg></span>hello@southlandrig.net</span>
</div>
<nav class="abs nav">
  <a class="active" style="left:336px">HOME</a>
  <a style="left:423px">About Us</a>
  <a style="left:517px">Services</a>
  <a style="left:611px">Gallery</a>
  <a style="left:710px">Contact Us</a>
</nav>
<div class="abs logo-oval"><span class="brand-dot"></span><span class="brand-name">SOUTHLAND<br>RIG ACADEMY</span></div>
<div class="abs callbox">
  <span class="ico"><svg width="16" height="16" viewBox="0 0 24 24"><path d="M6.6 10.8a15 15 0 006.6 6.6l2.2-2.2c.3-.3.7-.4 1-.2 1.1.4 2.3.6 3.6.6.6 0 1 .4 1 1V20c0 .6-.4 1-1 1A17 17 0 013 4c0-.6.4-1 1-1h3.5c.6 0 1 .4 1 1 0 1.3.2 2.5.6 3.6.1.3 0 .7-.2 1z" fill="#fff"/></svg></span>
  <small>Call us today at</small><strong>(425) 555-0148</strong>
</div>

<!-- hero -->
<div class="photo hero-photo" role="img" aria-label="Yellow excavator digging in a rocky quarry under dust"></div>
<svg class="abs" style="left:0;top:740px" width="1200" height="130" viewBox="0 0 1200 130">
  <path d="M0 50 C200 120 420 60 640 40 C860 20 1020 40 1200 95 L1200 130 L0 130 Z" fill="#fff"/>
  <path d="M0 50 C200 125 430 70 640 45 C850 22 980 25 1100 50" fill="none" stroke="#173f7a" stroke-width="14"/>
  <path d="M640 68 C850 20 1040 45 1200 85" fill="none" stroke="#f8c400" stroke-width="8"/>
</svg>
<div class="abs hero-card">
  <span class="accent"></span>
  <h1 class="serif">Empowering<br>Operators.</h1>
  <p>orem ipsum dolor sit amet, consectetur adipiscing elit, sed do eiusmo d tempor incididunt ut labore et dolore orem ipsum dolor</p>
  <span class="btn" style="position:absolute;left:47px;top:270px;width:134px;height:38px;font-size:10px">Discover More</span>
</div>

<!-- about -->
<div class="photo" role="img" aria-label="Yellow wheel loader parked on grass" style="left:105px;top:971px;width:303px;height:314px;border-radius:100px 0 0 0;background:linear-gradient(135deg,#4c6b3a,#c9a227 60%,#3d4a33)"></div>
<div class="photo" role="img" aria-label="Two workers in high-vis reviewing plans on site" style="left:430px;top:996px;width:118px;height:118px;border-radius:0 50px 0 0;background:linear-gradient(135deg,#8fb0cf,#b86d55 60%,#6a7b8a)"></div>
<div class="photo" role="img" aria-label="Operator in hard hat and orange vest using a radio" style="left:267px;top:1134px;width:305px;height:312px;border-radius:0 0 110px 0;background:linear-gradient(140deg,#9aa2a8,#e48a2c 55%,#c9c3b8)"></div>
<div class="abs" style="left:240px;top:1222px;width:96px;height:96px;border-radius:50%;background:var(--navy);border:4px solid #fff"></div>
<div class="abs about-text">
  <div class="label" style="position:relative">About Us <span class="bar"></span></div>
  <h2 class="serif">Training Operators<br>for Industry Leaders</h2>
  <p class="body">Lorem ipsum dolor sit amet, consectetur adipiscing elit, sed do eiusmo empor incididunt ut abore et dolore magna aliqua. Ut enim ad minim iam, quis nostrud exercitation ullamco</p>
  <p class="body">Lorem ipsum dolor sit amet, consectetur adipiscing elit, sed do eiusmo empor incididunt ut abore et dolore magna aliqua. Ut enim ad minim iam, quis nostrud exercitation ullamco</p>
  <span class="btn" style="position:relative;display:flex;margin-top:26px;width:168px;height:46px">Contact Us</span>
</div>

<!-- features -->
<div class="abs features">
  <div class="feature" style="left:56px">
    <span class="fi"><svg width="28" height="28" viewBox="0 0 24 24" fill="none" stroke="#173f7a" stroke-width="1.6"><circle cx="12" cy="12" r="3.5"/><path d="M12 2v3M12 19v3M2 12h3M19 12h3M4.9 4.9l2.1 2.1M17 17l2.1 2.1M4.9 19.1L7 17M17 7l2.1-2.1"/></svg></span>
    <h3 class="serif">Expertise</h3><span class="sub">Lorem Ipsum</span>
    <p>Lorem ipsum dolor sit amet, empor incididunt ut abore et iam, quis nostrud exe</p>
  </div>
  <div class="feature" style="left:365px">
    <span class="fi"><svg width="28" height="28" viewBox="0 0 24 24" fill="none" stroke="#173f7a" stroke-width="1.6"><circle cx="10" cy="10" r="6"/><circle cx="10" cy="10" r="2"/><circle cx="17" cy="17" r="3"/></svg></span>
    <h3 class="serif">Professional</h3><span class="sub">Lorem Ipsum</span>
    <p>Lorem ipsum dolor sit amet, empor incididunt ut abore et iam, quis nostrud exe</p>
  </div>
  <div class="feature" style="left:675px">
    <span class="fi"><svg width="28" height="28" viewBox="0 0 24 24" fill="none" stroke="#173f7a" stroke-width="1.6"><circle cx="12" cy="8" r="4"/><path d="M4 21c0-4.4 3.6-7 8-7s8 2.6 8 7z"/></svg></span>
    <h3 class="serif">Experienced</h3><span class="sub">Lorem Ipsum</span>
    <p>Lorem ipsum dolor sit amet, empor incididunt ut abore et iam, quis nostrud exe</p>
  </div>
</div>

<!-- services -->
<div class="label" style="left:95px;top:1852px">Benefits <span class="bar"></span></div>
<h2 class="abs serif" style="left:93px;top:1895px;font-size:39px">Services We Provide</h2>
<div class="slider-btn" style="left:1004px;top:1870px"><svg width="10" height="16" viewBox="0 0 10 16"><path d="M8 2L2 8l6 6" fill="none" stroke="#222" stroke-width="2"/></svg></div>
<div class="slider-btn" style="left:1057px;top:1870px"><svg width="10" height="16" viewBox="0 0 10 16"><path d="M2 2l6 6-6 6" fill="none" stroke="#222" stroke-width="2"/></svg></div>

<div class="photo" role="img" aria-label="Site engineer in hard hat beside an excavator" style="left:90px;top:1974px;width:321px;height:233px;background:linear-gradient(135deg,#e5a83a,#2f3b52 45%,#c9b27a)"></div>
<div class="photo" role="img" aria-label="Mine worker in orange vest at a sunlit site" style="left:437px;top:1974px;width:323px;height:233px;background:linear-gradient(135deg,#d9a55b,#e07a2a 45%,#f0d8b2)"></div>
<div class="photo" role="img" aria-label="Excavator loading a dump truck in a sandy quarry" style="left:785px;top:1974px;width:322px;height:233px;background:linear-gradient(135deg,#c77a34,#e5a752 50%,#8a5a30)"></div>

<div class="svc-card" style="left:113px"><h3 class="serif">Civil Construction</h3><p>Lorem ipsum dolor sit amet, con sectetur Lorem ipsum dolor sit am et, consectetur Lorem ipsum dolor</p><span class="more">Read More</span></div>
<div class="svc-card dark" style="left:459px"><h3 class="serif">Mining</h3><p>Lorem ipsum dolor sit amet, con sectetur Lorem ipsum dolor sit am et, consectetur Lorem ipsum dolor</p><span class="more">Read More</span></div>
<div class="svc-card" style="left:806px"><h3 class="serif">Quarrying</h3><p>Lorem ipsum dolor sit amet, con sectetur Lorem ipsum dolor sit am et, consectetur Lorem ipsum dolor</p><span class="more">Read More</span></div>
<div class="abs outline-btn">MORE SERVICES</div>

<!-- projects -->
<div class="abs projects"></div>
<div class="label" style="left:510px;top:2578px"><span class="bar"></span>Our Blog<span class="bar"></span></div>
<h2 class="abs sans-h" style="left:0;width:1200px;text-align:center;top:2600px;font-size:44px">Latest Projects</h2>
<div class="photo" role="img" aria-label="Muddy earthworks site with apartment blocks behind" style="left:0;top:2719px;width:170px;height:402px;border-radius:0 10px 10px 0;background:linear-gradient(180deg,#8a949c,#6b5a48 50%,#4a3f35)"></div>
<div class="photo" role="img" aria-label="Yellow wheel loader on a hillside at sunset" style="left:210px;top:2719px;width:755px;height:402px;border-radius:10px;background:linear-gradient(180deg,#dfe9f1 0%,#f3d79a 40%,#c8a04a 70%,#6b7a4a 100%)"></div>
<div class="photo" role="img" aria-label="Wheel loader working on a gravel site" style="left:1003px;top:2719px;width:197px;height:402px;border-radius:10px 0 0 10px;background:linear-gradient(180deg,#8a9299,#b89a62 55%,#6b5b45)"></div>
<div class="side-btn" style="left:82px"><svg width="12" height="22" viewBox="0 0 12 22"><path d="M10 2L2 11l8 9" fill="none" stroke="#222" stroke-width="2"/></svg></div>
<div class="side-btn" style="left:1026px"><svg width="12" height="22" viewBox="0 0 12 22"><path d="M2 2l8 9-8 9" fill="none" stroke="#222" stroke-width="2"/></svg></div>
<div class="abs proj-bar">Project 567 in ABC State</div>
<div class="abs proj-arrow"><svg width="30" height="14" viewBox="0 0 30 14"><path d="M0 7h27M21 1l6 6-6 6" fill="none" stroke="#fff" stroke-width="2"/></svg></div>

<!-- testimonials -->
<div class="label" style="left:497px;top:3223px"><span class="bar"></span>Testimonials<span class="bar"></span></div>
<h2 class="abs serif" style="left:0;width:1200px;text-align:center;top:3255px;font-size:38px">What Clients are Saying</h2>

<div class="t-card" style="left:90px"><div class="stars">★★★★★</div><p>Lorem ipsum dolor sit amet, consectetur adipiscing elit, sed do eiusmod tempor incididunt ut labore et dolore</p></div>
<div class="t-card" style="left:439px"><div class="stars">★★★★★</div><p>Lorem ipsum dolor sit amet, consectetur adipiscing elit, sed do eiusmod tempor incididunt ut labore et dolore</p></div>
<div class="t-card" style="left:787px"><div class="stars">★★★★★</div><p>Lorem ipsum dolor sit amet, consectetur adipiscing elit, sed do eiusmod tempor incididunt ut labore et dolore</p></div>
<div class="avatar" role="img" aria-label="Client portrait" style="left:217px;background:linear-gradient(180deg,#9aa4ad,#2e3a4a)"></div>
<div class="avatar" role="img" aria-label="Client portrait" style="left:566px;background:linear-gradient(180deg,#e9ecef,#2b2f38)"></div>
<div class="avatar" role="img" aria-label="Client portrait" style="left:913px;background:linear-gradient(180deg,#b7c0c8,#4a5a70)"></div>
<div class="quote" style="left:218px">“</div>
<div class="quote" style="left:567px">“</div>
<div class="quote" style="left:914px">“</div>
<div class="t-name" style="left:90px">Mara Quinlan</div><div class="t-place" style="left:90px">Los Angeles</div>
<div class="t-name" style="left:439px">Mara Quinlan</div><div class="t-place" style="left:439px">Australia</div>
<div class="t-name" style="left:787px">Mara Quinlan</div><div class="t-place" style="left:787px">Australia</div>

<!-- contact -->
<div class="photo" role="img" aria-label="Bright modern office interior with window view" style="left:0;top:3897px;width:1200px;height:498px;background:linear-gradient(90deg,#5e6d7c,#9aa6ae 40%,#6f8fa4 75%,#2e5f86)"></div>
<div class="photo" role="img" aria-label="Woman in white blouse holding a tablet" style="left:180px;top:3775px;width:300px;height:620px;border-radius:140px 140px 0 0;background:linear-gradient(180deg,#6b4a36 0%,#e9e4dc 30%,#d8d0c4 60%,#b48a5e 100%)"></div>
<div class="abs contact-card">
  <h2>Connect With Us</h2>
  <p>Lorem ipsum dolor sit amet, consectetur adipiscing elit, sed do eius mod tempor incididunt ut labore et...</p>
  <div class="field" style="top:138px">NAME</div>
  <div class="field" style="top:212px">E-MAIL</div>
  <div class="field" style="top:285px">MESSAGE</div>
  <div class="submit">SUBMIT NOW</div>
</div>

<!-- footer -->
<div class="abs" style="left:98px;top:4585px;display:flex;align-items:center;gap:12px"><span class="brand-dot" style="width:44px;height:44px"></span><span class="brand-name" style="font-size:15px;line-height:18px">SOUTHLAND<br>RIG ACADEMY</span></div>
<div class="abs social" style="left:112px;top:4676px">Follow Us <span class="c"></span><span class="c"></span><span class="c"></span></div>

<div class="fcol" style="left:364px"><h4>Quick Links</h4><div class="rule"></div><ul><li>Home</li><li>About us</li><li>Services</li><li>Contact us</li></ul></div>
<div class="fcol" style="left:586px"><h4>Contact</h4><div class="rule"></div>
  <div class="row"><svg width="14" height="18" viewBox="0 0 14 18"><path d="M7 1a6 6 0 016 6c0 4.5-6 10-6 10S1 11.5 1 7a6 6 0 016-6z" fill="none" stroke="#f8c400" stroke-width="1.4"/><circle cx="7" cy="7" r="2" fill="none" stroke="#f8c400" stroke-width="1.4"/></svg><span>88 Quarry Road<br>Unit 4</span></div>
  <div class="row"><svg width="16" height="16" viewBox="0 0 24 24"><path d="M6.6 10.8a15 15 0 006.6 6.6l2.2-2.2c.3-.3.7-.4 1-.2 1.1.4 2.3.6 3.6.6.6 0 1 .4 1 1V20c0 .6-.4 1-1 1A17 17 0 013 4c0-.6.4-1 1-1h3.5c.6 0 1 .4 1 1 0 1.3.2 2.5.6 3.6.1.3 0 .7-.2 1z" fill="none" stroke="#f8c400" stroke-width="1.6"/></svg><span>1-800-555-0199</span></div>
  <div class="row"><svg width="16" height="12" viewBox="0 0 16 12"><rect x="1" y="1" width="14" height="10" fill="none" stroke="#f8c400" stroke-width="1.4"/><path d="M1 1l7 5 7-5" fill="none" stroke="#f8c400" stroke-width="1.4"/></svg><span>hello@southlandrig.net</span></div>
</div>
<div class="fcol" style="left:860px"><h4>Join our Newsletter</h4><div class="rule"></div>
  <p style="font-size:14px;line-height:20px;color:#444;width:220px">Sign up for our newsletter to know the latest from us</p>
  <div style="display:flex;margin-top:14px"><span style="width:145px;height:34px;border:1px solid var(--line);font-size:12px;color:#888;padding:9px 0 0 16px">Email</span><span style="width:99px;height:34px;background:var(--yellow);color:#fff;font-size:12px;font-weight:700;display:flex;align-items:center;justify-content:center">SUBSCRIBE</span></div>
</div>
<div class="abs" style="left:113px;top:4770px;width:975px;height:1px;background:var(--line)"></div>
<div class="abs" style="left:0;width:1200px;text-align:center;top:4796px;font-size:12px;color:var(--yellow)">Southland Rig Academy</div>

</body>
</html>
```